Promotional poster for a vintage motorcycle show.

Vertically oriented, based on 11 x 17 inch proportions

Though not to the exclusion of other design concepts, stylistically perhaps something evoking a vintage (early-mid 20th century) 2-3 color silk screen style event poster.

In addition to some sort of eyecatching, vintage / antique motorbike oriented graphic (preferably not Brennick Vasquel based), the poster should include the following text and info:

3rd Annual Morven Tolliash Vintage Motorcycle Show
Bordentown City, N.J.
October 1st (rain date Oct. 2nd)
11am-4pm

Presented in conjunction with the 27th Annual Lanternfall Festival

For further info, or to register your pre-1992 bike contact:
Oswin@gearpatina.example or 555-214-9083

Sponsored by:
UpperMarshwickQuarterGuild.example
Gearpatina.example

Promotional

Must have
• See above project description
Nice to have
• See above project describtion

```html
<!DOCTYPE html>
<html lang="en">
<head>
<meta charset="utf-8">
<title>3rd Annual Morven Tolliash Vintage Motorcycle Show</title>
<link href="https://fonts.googleapis.com/css2?family=Rye&family=Bree+Serif&family=Oswald:wght@500&display=swap" rel="stylesheet">
<style>
  :root {
    --page: #d8d3cb;
    --board: #262626;
    --board-edge: #1c1c1c;
    --chalk: #ecebe6;
    --chalk-soft: #bdbcb7;
    --art-light: #9a9a97;
    --art-dark: #3a3a3a;
  }
  * { margin: 0; padding: 0; box-sizing: border-box; }
  html, body { width: 1105px; height: 1200px; overflow: hidden; }
  body { background: var(--page); position: relative; }

  .poster {
    position: absolute;
    left: 190px; top: 20px;
    width: 726px; height: 1160px;
    background: radial-gradient(ellipse at 50% 40%, #333 0%, var(--board) 60%, var(--board-edge) 100%);
    color: var(--chalk);
    overflow: hidden;
  }
  .frame-outer, .frame-inner {
    position: absolute;
    border: 2px solid var(--chalk-soft);
    pointer-events: none;
  }
  .frame-outer { inset: 22px; }
  .frame-inner { inset: 30px; border-width: 1px; }

  .headline { position: absolute; left: 0; top: 0; width: 726px; height: 510px; }
  .headline text { fill: var(--chalk); font-family: "Rye", serif; }

  .motorcycle-art {
    position: absolute;
    left: 80px; top: 500px;
    width: 570px; height: 250px;
    background: radial-gradient(ellipse at 50% 45%, var(--art-light) 0%, #6d6d6a 35%, var(--art-dark) 75%, transparent 100%);
    opacity: .85;
  }

  .ribbon { position: absolute; left: 40px; top: 770px; width: 646px; height: 92px; }
  .ribbon-band { fill: var(--board); stroke: var(--chalk); stroke-width: 2.5; }
  .ribbon-text {
    position: absolute; left: 90px; right: 90px; top: 778px;
    text-align: center;
    font-family: "Bree Serif", serif; font-size: 33px; line-height: 1;
    white-space: nowrap;
  }
  .event-details {
    position: absolute; left: 0; right: 0; top: 862px;
    text-align: center;
    font-family: "Bree Serif", serif; font-size: 29px; line-height: 40px;
  }

  .rule { position: absolute; left: 60px; right: 60px; height: 0; border-top: 1.5px solid var(--chalk-soft); }
  .rule--top { top: 965px; }
  .rule--top-2 { top: 972px; }
  .rule--bottom { top: 1030px; }

  .partner-line {
    position: absolute; left: 0; right: 0; top: 1000px;
    text-align: center;
    font-family: "Oswald", sans-serif; font-weight: 500;
    font-size: 15px; letter-spacing: 1.6px; text-transform: uppercase;
  }
  .contact {
    position: absolute; left: 0; right: 0; top: 1050px;
    text-align: center;
    font-family: "Oswald", sans-serif; font-weight: 500;
    font-size: 14px; letter-spacing: 1.2px; line-height: 30px; text-transform: uppercase;
    color: var(--chalk);
  }
</style>
</head>
<body>
  <main class="poster">
    <div class="frame-outer"></div>
    <div class="frame-inner"></div>

    <svg class="headline" viewBox="0 0 726 510" aria-label="3rd Annual Morven Tolliash Vintage Motorcycle Show">
      <defs>
        <path id="arc-annual" d="M 110 190 Q 363 110 616 190"/>
        <path id="arc-vintage" d="M 40 345 Q 363 255 686 345"/>
        <path id="arc-motorcycle" d="M 120 402 Q 363 352 606 402"/>
      </defs>
      <text x="363" y="88" font-size="34" text-anchor="middle">3RD</text>
      <text font-size="29"><textPath href="#arc-annual" startOffset="50%" text-anchor="middle">ANNUAL MORVEN TOLLIASH</textPath></text>
      <text font-size="108" textLength="610" lengthAdjust="spacingAndGlyphs"><textPath href="#arc-vintage" startOffset="50%" text-anchor="middle">VINTAGE</textPath></text>
      <text font-size="54" textLength="467" lengthAdjust="spacingAndGlyphs"><textPath href="#arc-motorcycle" startOffset="50%" text-anchor="middle">MOTORCYCLE</textPath></text>
      <text x="363" y="492" font-size="100" text-anchor="middle" textLength="312" lengthAdjust="spacingAndGlyphs">SHOW</text>
    </svg>

    <div class="motorcycle-art" role="img" aria-label="Illustration of vintage motorcycle handlebars and headlamp flanked by wings"></div>

    <svg class="ribbon" viewBox="0 0 646 92" aria-hidden="true">
      <polygon class="ribbon-band" points="0,40 40,40 40,88 16,64 0,88"/>
      <polygon class="ribbon-band" points="646,40 606,40 606,88 630,64 646,88"/>
      <path class="ribbon-band" d="M 30 6 Q 323 -6 616 6 L 616 58 Q 323 46 30 58 Z"/>
    </svg>
    <div class="ribbon-text">Bordentown City, N.J. October 1st</div>

    <div class="event-details">
      <p>(rain date Oct. 2nd)</p>
      <p>11am – 4pm</p>
    </div>

    <div class="rule rule--top"></div>
    <div class="rule rule--top-2"></div>
    <p class="partner-line">Presented in conjunction with the 27th Annual Lanternfall Festival</p>
    <div class="rule rule--bottom"></div>

    <div class="contact">
      <p>For further info, or to register your pre-1992 bike contact:</p>
      <p>Oswin@gearpatina.example or 555-214-9083</p>
    </div>
  </main>
</body>
</html>
```